Print materials for 3-star hotel

We are changing up our print materials (notepads, letterheads, key card jackets, small flyer for the room rates) We are a 3 star business hotel in the Philippines and have mainly used grey tones and clean, simple lines. See attached photos for logo and hotel interior photos.

Target Market(s)

Business

Contact Information for Business Card

Corvina Terrace Hotel
Magistrate Lunod Avenue corner Pabilo St Cebu City 6000 Philippines
Tel: +63 32 481 7520
Mobile: +63 917 604 2893
www.corvinaterracehotel.example

Font styles to use
Serif
Sans Serif

Requirements
Must have
• Simple
• Readable font and font size
Nice to have
• Neutral colors, grey and taupes
Should not have
• No purples and bright blues

```html
<!DOCTYPE html>
<html lang="en">
<head>
<meta charset="utf-8">
<title>Corvina Terrace Hotel – Business Card</title>
<link rel="stylesheet" href="https://fonts.googleapis.com/css2?family=Cinzel:wght@400&family=Montserrat:wght@400;600;700&display=swap">
<style>
  :root {
    --page: #ececec;
    --card-grey: #9b9b9b;
    --band-grey: #a3a3a3;
    --card-white: #f6f6f6;
    --ink: #7a7a7a;
    --ink-strong: #6a6a6a;
    --on-grey: #f2f2f2;
    --rule: #b8b8b8;
  }
  * { box-sizing: border-box; margin: 0; padding: 0; }
  html, body { width: 1200px; height: 1167px; overflow: hidden; }
  body {
    background: var(--page);
    font-family: "Montserrat", Arial, sans-serif;
    display: flex;
    flex-direction: column;
    align-items: center;
    justify-content: center;
    gap: 56px;
  }
  .card {
    width: 840px;
    height: 480px;
    position: relative;
    overflow: hidden;
    box-shadow: 0 6px 18px rgba(0,0,0,0.12);
  }

  /* Front */
  .card-front {
    background: var(--card-grey);
    display: flex;
    align-items: center;
    justify-content: center;
  }
  .front-texture { position: absolute; inset: 0; background: linear-gradient(135deg, #a1a1a1, #959595); }
  .front-brand {
    position: relative;
    text-align: center;
    color: var(--on-grey);
    font-family: "Cinzel", Georgia, serif;
    font-weight: 400;
  }
  .front-brand .mark {
    display: block;
    width: 64px; height: 64px;
    margin: 0 auto 26px;
    background: var(--on-grey);
  }
  .front-brand .name { font-size: 44px; letter-spacing: 10px; line-height: 1.1; }
  .front-brand .sub { font-size: 30px; letter-spacing: 12px; margin-top: 6px; }

  /* Back */
  .card-back { background: var(--card-white); }
  .band { position: absolute; left: 0; right: 0; height: 82px; background: var(--band-grey); }
  .band-top { top: 0; }
  .band-bottom { bottom: 0; }
  .back-body {
    position: absolute;
    top: 82px; bottom: 82px; left: 0; right: 0;
    display: flex;
    align-items: center;
  }
  .col-left { width: 420px; padding: 0 40px 0 60px; }
  .divider { width: 1px; height: 220px; background: var(--rule); }
  .col-right { flex: 1; padding-left: 44px; }

  .back-brand {
    font-family: "Montserrat", Arial, sans-serif;
    font-weight: 700;
    font-size: 26px;
    color: var(--ink);
    letter-spacing: 1px;
    margin-bottom: 22px;
    line-height: 1.2;
  }
  .address { font-size: 17px; line-height: 1.45; color: var(--ink); font-style: normal; }
  .address strong { font-weight: 700; color: var(--ink-strong); }

  .person-name { font-size: 27px; font-weight: 700; color: var(--ink-strong); }
  .person-title { font-size: 16px; color: var(--ink); margin-bottom: 22px; }
  .contacts { list-style: none; }
  .contacts li {
    display: flex; align-items: center; gap: 12px;
    font-size: 17px; color: var(--ink); line-height: 1.6;
  }
  .contacts svg { width: 16px; height: 16px; flex: none; }
  .contacts li.web { padding-left: 28px; }
</style>
</head>
<body>

  <section class="card card-front">
    <div class="front-texture" role="img" aria-label="Fine wavy line pattern in grey tones"></div>
    <div class="front-brand">
      <span class="mark"></span>
      <div class="name">Corvina Terrace</div>
      <div class="sub">Hotel</div>
    </div>
  </section>

  <section class="card card-back">
    <div class="band band-top" role="img" aria-label="Grey band with fine wavy line pattern"></div>
    <div class="back-body">
      <div class="col-left">
        <div class="back-brand">Corvina Terrace Hotel</div>
        <address class="address">
          Magistrate Lunod Avenue corner<br>
          Pabilo St, Cebu City<br>
          Cebu, 6000, <strong>Philippines</strong>
        </address>
      </div>
      <div class="divider"></div>
      <div class="col-right">
        <div class="person-name">Adrian VELASCO</div>
        <div class="person-title">Managing Director</div>
        <ul class="contacts">
          <li><svg viewBox="0 0 16 16"><circle cx="8" cy="8" r="7" fill="none" stroke="#7a7a7a" stroke-width="1.2"/><path d="M5.5 4.5l1.5 1.5-1 1a5 5 0 0 0 3 3l1-1 1.5 1.5-1 1c-3 0-6-3-6-6z" fill="#7a7a7a"/></svg>+63 32 481 7520</li>
          <li><svg viewBox="0 0 16 16"><circle cx="8" cy="8" r="7" fill="none" stroke="#7a7a7a" stroke-width="1.2"/><path d="M5.5 4.5l1.5 1.5-1 1a5 5 0 0 0 3 3l1-1 1.5 1.5-1 1c-3 0-6-3-6-6z" fill="#7a7a7a"/></svg>+63 917 604 2893</li>
          <li><svg viewBox="0 0 16 16"><circle cx="8" cy="8" r="7" fill="none" stroke="#7a7a7a" stroke-width="1.2"/><path d="M5.5 4.5l1.5 1.5-1 1a5 5 0 0 0 3 3l1-1 1.5 1.5-1 1c-3 0-6-3-6-6z" fill="#7a7a7a"/></svg>+63 918 730 4412</li>
          <li><svg viewBox="0 0 16 16"><circle cx="8" cy="8" r="7" fill="none" stroke="#7a7a7a" stroke-width="1.2"/><rect x="4.5" y="5.5" width="7" height="5" fill="none" stroke="#7a7a7a" stroke-width="1"/><path d="M4.5 5.5L8 8.5l3.5-3" fill="none" stroke="#7a7a7a" stroke-width="1"/></svg>adrian@corvinaterracehotel.example</li>
          <li class="web">www.corvinaterracehotel.example</li>
        </ul>
      </div>
    </div>
    <div class="band band-bottom" role="img" aria-label="Grey band with fine wavy line pattern"></div>
  </section>

</body>
</html>
```